Website for my photography business

I need a website for my photography business, Jonah Pelling Photography. I need a website that has a landing page with a cover photo of each kind of photography I do. For example, Nature, Weddings, Portraits and Architecture. I want it so that when someone comes onto my website they have to choose which kind of photography page they want to visit. So if they click on the wedding photo it will open to a page with my wedding portfolio images and a contact me button. If they choose nature photography I want them to be redirected to an e-commerce section where they can purchase prints. Architecture and Portraits should open up to their respective portfolios with about me and contact info. I like this kind of format because I want people who come to my website for a specific type of photography to be able to be directed there easily without having to look at a mix of other kinds of photography. I will provide a few files to use as placeholders. I have already purchased the jonahpellingphotography.example domain name. A Wix website would be great because I am most familiar with it but I am open to anything.

Industry/Entity Type

Photographer

Number of Pages Required

5+ page

Requirements
Must have
• Landing Page and e-commerce

```html
<!DOCTYPE html>
<html lang="en">
<head>
<meta charset="utf-8">
<title>Jonah Pelling Photography</title>
<link href="https://fonts.googleapis.com/css2?family=Lato:wght@400;700;900&display=swap" rel="stylesheet">
<style>
  :root {
    --page-bg: #2b2b2b;
    --band-bg: #343434;
    --nav-line: #4a4a4a;
    --nav-active-top: #44484a;
    --text-light: #ffffff;
    --text-soft: #d2d2d2;
    --text-muted: #7a7a7a;
    --button-bg: #8a8a8a;
    --button-text: #dcdcdc;
    --chip-bg: rgba(220, 220, 220, 0.72);
    --chip-text: #333333;
    --icon: #8f8f8f;
    --star: #f2c21b;
  }
  * { margin: 0; padding: 0; box-sizing: border-box; }
  html, body { width: 1200px; height: 1059px; overflow: hidden; }
  body {
    background: var(--page-bg);
    font-family: "Lato", Arial, sans-serif;
    position: relative;
  }
  .site-header { position: absolute; left: 0; top: 0; width: 1200px; height: 216px; }
  .brand {
    position: absolute; left: 43px; top: 70px;
    color: var(--text-light);
  }
  .brand-name {
    font-size: 30px; font-weight: 400; letter-spacing: 0.5px;
    display: flex; align-items: center; gap: 10px;
  }
  .brand-mark { width: 10px; height: 10px; border-radius: 50%; background: var(--star); display: inline-block; }
  .brand-tagline { font-size: 9px; margin-top: 6px; margin-left: 110px; color: var(--text-light); }
  .main-nav { position: absolute; top: 0; left: 597px; height: 170px; display: flex; }
  .nav-item {
    height: 170px; border-left: 1px solid var(--nav-line);
    display: flex; align-items: flex-end; justify-content: center;
    padding-bottom: 8px;
    color: var(--text-light); font-size: 17px; text-decoration: none;
  }
  .nav-item:last-child { border-right: 1px solid var(--nav-line); }
  .nav-item.is-active { background: linear-gradient(to bottom, var(--nav-active-top), var(--page-bg)); }
  .gallery-band {
    position: absolute; left: 0; top: 216px; width: 1200px; height: 433px;
    background: var(--band-bg);
  }
  .category {
    position: absolute; top: 1px; width: 273px; height: 432px;
    display: flex; flex-direction: column; align-items: center; justify-content: flex-end;
    padding-bottom: 30px; text-decoration: none;
  }
  .category-photo { position: absolute; inset: 0; }
  .category-title {
    position: relative; color: var(--text-light); font-weight: 900;
    font-size: 35px; line-height: 1; margin-bottom: 12px;
  }
  .category-link {
    position: relative; background: var(--chip-bg); color: var(--chip-text);
    font-size: 14px; width: 130px; height: 32px;
    display: flex; align-items: center; justify-content: center;
  }
  .nature { left: 36px; }
  .nature .category-photo { background: linear-gradient(160deg, #9a9ea3 0%, #6f7a86 40%, #5a4a3a 75%, #3b3128 100%); }
  .wedding { left: 321px; }
  .wedding .category-photo { background: linear-gradient(170deg, #c9c9c9 0%, #8f8f8f 45%, #3a3a3a 70%, #d8d8d8 100%); }
  .portrait { left: 606px; }
  .portrait .category-photo { background: linear-gradient(165deg, #9fb6c4 0%, #6d5a50 40%, #4a4a4a 65%, #9c8f84 100%); }
  .architecture { left: 891px; }
  .architecture .category-photo { background: linear-gradient(180deg, #cfd6dc 0%, #b9bfc4 20%, #8c4a36 45%, #7a6a60 75%, #8a9a6a 100%); }
  .intro {
    position: absolute; top: 700px; left: 60px; width: 1080px;
    text-align: center; color: var(--text-soft); font-size: 25px; line-height: 35px;
  }
  .contact-button {
    position: absolute; left: 258px; top: 822px; width: 684px; height: 82px;
    background: var(--button-bg); color: var(--button-text);
    font-size: 30px; font-weight: 700;
    display: flex; align-items: center; justify-content: center; text-decoration: none;
  }
  .social-links { position: absolute; top: 937px; left: 496px; display: flex; gap: 18px; }
  .social-link { width: 27px; height: 27px; border-radius: 50%; background: var(--icon); display: block; }
  .copyright {
    position: absolute; top: 1007px; left: 0; width: 1200px; text-align: center;
    color: var(--text-muted); font-size: 15px;
  }
</style>
</head>
<body>
  <header class="site-header">
    <div class="brand">
      <div class="brand-name">Jonah Pelling Photography <span class="brand-mark"></span></div>
      <div class="brand-tagline">Creating extraordinary images that last infinitely</div>
    </div>
    <nav class="main-nav">
      <a class="nav-item is-active" href="#" style="width:136px">Home</a>
      <a class="nav-item" href="#" style="width:134px">About&nbsp; Me</a>
      <a class="nav-item" href="#" style="width:155px">What We do</a>
      <a class="nav-item" href="#" style="width:141px">Contact Me</a>
    </nav>
  </header>

  <section class="gallery-band">
    <a class="category nature" href="#">
      <div class="category-photo" role="img" aria-label="Cover photo: small grey songbird perched on a weathered branch"></div>
      <span class="category-title">NATURE</span>
      <span class="category-link">SEE GALLERY</span>
    </a>
    <a class="category wedding" href="#">
      <div class="category-photo" role="img" aria-label="Cover photo: black and white portrait of a bride and groom embracing"></div>
      <span class="category-title">WEDDING</span>
      <span class="category-link">SEE GALLERY</span>
    </a>
    <a class="category portrait" href="#">
      <div class="category-photo" role="img" aria-label="Cover photo: woman in a beret and fur coat posing outdoors"></div>
      <span class="category-title">PORTRAIT</span>
      <span class="category-link">SEE GALLERY</span>
    </a>
    <a class="category architecture" href="#">
      <div class="category-photo" role="img" aria-label="Cover photo: modern brick building with glass balcony"></div>
      <span class="category-title">ARCHITECTURE</span>
      <span class="category-link">SEE GALLERY</span>
    </a>
  </section>

  <p class="intro">We are a photography studio specializing in portrait, nature and conceptual photography, based in New York. We love to turn ideas into beautiful things.</p>

  <a class="contact-button" href="#">Contact Me</a>

  <nav class="social-links" aria-label="Social media">
    <a class="social-link" href="#" aria-label="Messaging"></a>
    <a class="social-link" href="#" aria-label="Video channel"></a>
    <a class="social-link" href="#" aria-label="Microblog"></a>
    <a class="social-link" href="#" aria-label="Social network"></a>
    <a class="social-link" href="#" aria-label="Photo sharing"></a>
  </nav>

  <footer class="copyright">© 2011 Pelling Studio, All Rights Reserved</footer>
</body>
</html>
```